Local Horticulturalist needs Business card design

Meridale Gardening would like to update our existing business card and utilize our new logo (design attached)....we specialize in getting the best out of our customers yard with professional maintenance programs, expert pruning and hedging and garden restorations.
Utilizing colors from attached logo I would like a design that implies professionalism and if possible our businesses love of restoration through plants.
I also sometimes write down for my customers a start date and price on the back of my current card
Target Market(s)
Home owners
Contractors
Industry/Entity Type
Gardener
Contact Information for Business Card
Trevor Kalbrook | Horticulturalist
ph: 0452739186
meridalegard@fernpost.com
www.meridalegardening.com.au
Requirements
Must have
- crucial information easy to read
- incorporate current logo
- Horticulturalist listed preferably near name
Nice to have
- currently I write a job start date and price on the back of my current card so something that integrates this would be beneficial
Should not have
- be pretty or flowerey
- be too white or basic

```html
<!DOCTYPE html>
<html lang="en">
<head>
<meta charset="utf-8">
<title>Meridale Gardening – Business Card</title>
<link href="https://fonts.googleapis.com/css2?family=Hind:wght@400;600&family=Roboto+Condensed:wght@500;600&display=swap" rel="stylesheet">
<style>
  :root {
    --leaf-green: #80a05a;
    --label-green: #76a04e;
    --bark-brown: #7a6a55;
    --text-brown: #6b5a45;
    --mark-green: #8cc043;
    --card-edge: #111111;
    --paper: #ffffff;
  }
  * { margin: 0; padding: 0; box-sizing: border-box; }
  html, body {
    width: 927px; height: 1200px; overflow: hidden;
    background: var(--paper);
  }
  .sheet { position: relative; width: 927px; height: 1200px; }
  .card {
    position: absolute; left: 116px; width: 695px; height: 398px;
    border: 2px solid var(--card-edge); background: var(--paper);
    overflow: hidden;
  }
  .card--front { top: 105px; }
  .card--back { top: 695px; }

  .brand-dot { position: absolute; border-radius: 50%; background: var(--mark-green); }
  .card--front .brand-dot { left: 34px; top: 59px; width: 124px; height: 124px; }
  .card--back .brand-dot { left: 40px; top: 47px; width: 90px; height: 90px; }

  .person {
    position: absolute; left: 180px; top: 66px;
    font-family: "Hind", sans-serif; color: var(--bark-brown);
  }
  .person__name { font-size: 46px; font-weight: 600; line-height: 54px; }
  .person__role { font-size: 46px; font-weight: 400; line-height: 50px; }

  .contact {
    position: absolute; left: 36px; top: 262px; list-style: none;
    font-family: "Roboto Condensed", sans-serif; font-weight: 600;
    font-size: 25px; line-height: 33px; color: var(--text-brown);
  }
  .contact__label { color: var(--label-green); }

  .business {
    position: absolute; left: 143px; top: 56px;
    font-family: "Hind", sans-serif; color: var(--bark-brown);
  }
  .business__name { font-size: 46px; font-weight: 600; line-height: 50px; }
  .business__tagline { font-size: 21px; font-weight: 400; letter-spacing: 1px; line-height: 24px; }

  .job-band {
    position: absolute; left: 0; bottom: 0; width: 100%; height: 134px;
    background: var(--leaf-green);
    font-family: "Roboto Condensed", sans-serif; font-weight: 500;
    font-size: 25px; color: var(--paper);
  }
  .job-band__label { position: absolute; top: 56px; }
  .job-band__label--date { left: 36px; }
  .job-band__label--price { left: 448px; }
  .job-band__field { position: absolute; top: 43px; height: 54px; background: var(--paper); }
  .job-band__field--date { left: 230px; width: 187px; }
  .job-band__field--price { left: 523px; width: 134px; }
</style>
</head>
<body>
<main class="sheet">
  <section class="card card--front">
    <span class="brand-dot"></span>
    <div class="person">
      <p class="person__name">Trevor Kalbrook</p>
      <p class="person__role">Horticulturist</p>
    </div>
    <ul class="contact">
      <li><span class="contact__label">PHONE</span> | 045·273·9186</li>
      <li><span class="contact__label">EMAIL</span> | meridalegard@fernpost.com</li>
      <li><span class="contact__label">WEB</span> | www.meridalegardening.com.au</li>
    </ul>
  </section>

  <section class="card card--back">
    <span class="brand-dot"></span>
    <div class="business">
      <p class="business__name">Meridale Gardening</p>
      <p class="business__tagline">Garden Restorations &amp; Maintenance</p>
    </div>
    <div class="job-band">
      <span class="job-band__label job-band__label--date">JOB START DATE</span>
      <span class="job-band__field job-band__field--date"></span>
      <span class="job-band__label job-band__label--price">PRICE</span>
      <span class="job-band__field job-band__field--price"></span>
    </div>
  </section>
</main>
</body>
</html>
```